Dental Practice Billboard Design

We are a newer dental practice in need of a simple but appealing billboard for our growing dental practice to attract new patients. The practice is owned by husband and wife dentists and is family friendly in a small town in Kentucky. We try to be very friendly and caring to our patients. Would prefer a blue background for the billboard and our tooth logo to be prominent. We are partial to the Patua One font used in the image below but please feel free to tweak it as you deem necessary. The shape of the uppercase D and lowercase g are why we like that font, so fonts with a similarly shaped “D” and “g” would work as well. Please include our phone number (606) 847-3962. Please see our website Harlowfamilydentistry.com for more info on the practice if needed. Thank you! Looking forward to seeing your creation.
Updates

The dimensions will be 12ft x 24ft (3.6576m x 7.3152m). Apologies for not including this in the original prompt. Thank you all for your submissions.

Industry/Entity Type

Dental

Font styles to use
Other font styles liked:
• Patua One

Colors
0054AA
0677BA
7BADD7
CADEEF
E8F1F8
0094D4
00A9DD
6FCCEA
C7EBF8
E9F6FB
00AB8E
00BBA5
67D7C9
C6EFE9
E9F9F6
59FF00
82FF00
B8FF75
E3FFCB
F4FFEA

Requirements
Must have
• Phone number, website, Logo, Practice name “Harlow Family Dentistry”
Should not have
• A tagline or slogan

```html
<!DOCTYPE html>
<html lang="en">
<head>
<meta charset="utf-8">
<title>Harlow Family Dentistry — Billboard</title>
<link rel="stylesheet" href="https://fonts.googleapis.com/css2?family=Patua+One&family=Asap+Condensed:wght@600&display=swap">
<style>
  :root {
    --page-grey: #bdbdbd;
    --board-blue: #2a5aa8;
    --brand-green: #22b24c;
    --white: #ffffff;
    --photo-warm: #c9a58a;
    --photo-light: #efe6dc;
    --phone-icon: #1a6b3a;
  }
  * { margin: 0; padding: 0; box-sizing: border-box; }
  html, body {
    width: 1200px;
    height: 823px;
    overflow: hidden;
    background: var(--page-grey);
  }
  .billboard {
    position: absolute;
    left: 40px;
    top: 132px;
    width: 1042px;
    height: 520px;
    transform: scale(1.075);
    transform-origin: 0 0;
    background: var(--board-blue);
    overflow: hidden;
  }
  .practice-title {
    position: absolute;
    left: 88px;
    top: 162px;
    font-family: "Patua One", serif;
    font-weight: 400;
    font-size: 74px;
    line-height: 88px;
    color: var(--white);
  }
  .practice-title span { display: block; }
  .website {
    position: absolute;
    left: 94px;
    top: 440px;
    font-family: "Patua One", serif;
    font-size: 19px;
    color: var(--white);
  }
  .photo-frame {
    position: absolute;
    left: 414px;
    top: 84px;
    width: 300px;
    height: 394px;
    border-radius: 150px 150px 60px 60px / 130px 130px 60px 60px;
    border-left: 20px solid var(--white);
    border-right: 20px solid var(--brand-green);
    background: linear-gradient(160deg, var(--photo-light) 0%, var(--photo-warm) 55%, #f4f4f4 100%);
    background-clip: padding-box;
  }
  .brand-name {
    position: absolute;
    left: 816px;
    top: 86px;
    width: 200px;
    display: flex;
    align-items: center;
    gap: 10px;
    font-family: "Patua One", serif;
    font-size: 22px;
    line-height: 1.1;
    color: var(--white);
  }
  .brand-name .brand-dot {
    width: 16px;
    height: 16px;
    border-radius: 50%;
    background: var(--brand-green);
    flex: none;
  }
  .phone-pill {
    position: absolute;
    left: 710px;
    top: 397px;
    width: 293px;
    height: 61px;
    border-radius: 31px;
    background: var(--brand-green);
    display: flex;
    align-items: center;
    gap: 12px;
    padding-left: 18px;
    font-family: "Asap Condensed", sans-serif;
    font-weight: 600;
    font-size: 33px;
    color: var(--white);
  }
  .phone-pill svg { width: 30px; height: 30px; flex: none; }
</style>
</head>
<body>
  <main class="billboard">
    <h1 class="practice-title">
      <span>Harlow</span>
      <span>Family</span>
      <span>Dentistry</span>
    </h1>
    <p class="website">Harlowfamilydentistry.com</p>

    <div class="photo-frame" role="img" aria-label="Photo of the two smiling dentists in white coats inside the practice"></div>

    <div class="brand-name">
      <span class="brand-dot"></span>
      <span>Harlow Family Dentistry</span>
    </div>

    <div class="phone-pill">
      <svg viewBox="0 0 24 24" aria-hidden="true">
        <path fill="var(--phone-icon)" d="M6.6 10.8c1.4 2.8 3.8 5.1 6.6 6.6l2.2-2.2c.3-.3.7-.4 1-.2 1.1.4 2.3.6 3.6.6.6 0 1 .4 1 1V20c0 .6-.4 1-1 1C10.6 21 3 13.4 3 4c0-.6.4-1 1-1h3.5c.6 0 1 .4 1 1 0 1.3.2 2.5.6 3.6.1.3 0 .7-.2 1l-2.3 2.2z"/>
        <path fill="none" stroke="var(--phone-icon)" stroke-width="1.6" stroke-linecap="round" d="M14.5 3.5a6 6 0 0 1 6 6M14.5 6.8a2.8 2.8 0 0 1 2.8 2.8"/>
      </svg>
      <span>(606) 847-3962</span>
    </div>
  </main>
</body>
</html>
```